church business card design

we have a logo and would like our business card to complement the logo. we would prefer the logo in white on a coloured background - probably blue. Under the logo or near it we would have the Words 'Love God. Love people. Follow Jesus.'
We would like some yellow/gold highlights. We like the design by mintaro quill 4821 front of card - https://www.pelvarostudio.com/businesscard-design/contest/5812094

Our church is multicultural, inner city, friendly, warm welcoming and that's the feel we would like. there's also an element of being spontaneous, so a swirl or swoosh might help give that feel. the example card above had some curved shapes on the front of the card for example.
on the second side of the card would have the details of the Senior Pastor and the contact details for the church.
after the business card we would be looking at letterhead and an A5 flyer for printing but also as document templates so we can create invitations etc going forward

```html
<!DOCTYPE html>
<html lang="en">
<head>
<meta charset="utf-8">
<title>Cornerway Church – Business Card</title>
<link href="https://fonts.googleapis.com/css2?family=Archivo:wght@400;800&display=swap" rel="stylesheet">
<style>
  :root {
    --stage: #3a3a3c;
    --blue-deep: #23308f;
    --blue: #2f40be;
    --blue-bright: #3a4fd6;
    --gold: #e8b52e;
    --white: #ffffff;
    --ink-blue: #1f2a86;
  }
  * { box-sizing: border-box; margin: 0; padding: 0; }
  html, body { width: 1200px; height: 1015px; overflow: hidden; }
  body {
    background: var(--stage);
    font-family: "Archivo", Arial, sans-serif;
    position: relative;
  }
  .card {
    position: absolute;
    width: 700px;
    height: 400px;
    overflow: hidden;
    box-shadow: 0 18px 40px rgba(0,0,0,.55);
  }
  /* Front */
  .card-front {
    left: 90px; top: 70px;
    background: linear-gradient(180deg, var(--blue-deep) 0%, var(--blue-bright) 45%, var(--blue-deep) 80%);
  }
  .church-name {
    position: absolute;
    left: 0; right: 0; top: 150px;
    text-align: center;
    color: var(--gold);
    font-family: "Archivo", Arial, sans-serif;
    font-weight: 800;
    font-size: 48px;
    line-height: 1;
  }
  .tagline-band {
    position: absolute;
    left: 0; right: 0; top: 292px; height: 52px;
    background: var(--gold);
    display: flex; align-items: center; justify-content: center;
  }
  .tagline {
    font-family: "Archivo", Arial, sans-serif;
    font-weight: 800;
    color: var(--ink-blue);
    font-size: 21px;
    letter-spacing: 1.5px;
  }
  /* Back */
  .card-back {
    left: 410px; top: 545px;
    background: linear-gradient(180deg, var(--blue-deep) 0%, var(--blue-bright) 50%, var(--blue-deep) 100%);
  }
  .hill-cross-art {
    position: absolute;
    right: 0; top: 0;
    width: 330px; height: 400px;
  }
  .contact {
    position: absolute;
    left: 48px; top: 150px;
    color: var(--white);
  }
  .person-name { font-weight: 800; font-size: 30px; letter-spacing: .5px; line-height: 1.05; }
  .person-role { font-size: 19px; margin-bottom: 16px; }
  .contact-line { display: flex; align-items: center; gap: 10px; font-size: 19px; line-height: 1.35; }
  .contact-line svg { width: 18px; height: 18px; flex: none; }
  .address { margin-top: 18px; padding-left: 28px; font-size: 19px; line-height: 1.3; }
</style>
</head>
<body>

  <section class="card card-front">
    <p class="church-name">Cornerway Church</p>
    <div class="tagline-band">
      <p class="tagline">Love God. Love People. Follow Jesus</p>
    </div>
  </section>

  <section class="card card-back">
    <svg class="hill-cross-art" viewBox="0 0 330 400" role="img" aria-label="Faint cross standing on a hill illustration">
      <defs>
        <linearGradient id="art-tone" x1="0" y1="0" x2="0" y2="1">
          <stop offset="0" stop-color="#2a39ad" stop-opacity=".6"/>
          <stop offset="1" stop-color="#3b50d8" stop-opacity=".5"/>
        </linearGradient>
      </defs>
      <path d="M0 400 Q120 300 330 260 L330 0 L40 0 Z" fill="url(#art-tone)"/>
    </svg>

    <div class="contact">
      <h1 class="person-name">MARCUS ELLERY</h1>
      <p class="person-role">Managing Director</p>
      <p class="contact-line">
        <svg viewBox="0 0 24 24"><path fill="#fff" d="M6.6 10.8a15 15 0 0 0 6.6 6.6l2.2-2.2c.3-.3.7-.4 1-.2 1.1.4 2.3.6 3.6.6.6 0 1 .4 1 1V20c0 .6-.4 1-1 1A17 17 0 0 1 3 4c0-.6.4-1 1-1h3.5c.6 0 1 .4 1 1 0 1.3.2 2.5.6 3.6.1.3 0 .7-.2 1z"/></svg>
        041-552 730 418
      </p>
      <p class="contact-line">
        <svg viewBox="0 0 24 24"><path fill="#fff" d="M2 5h20v14H2zM3.5 6.5 12 13l8.5-6.5z"/></svg>
        hello@cornerway.org
      </p>
      <p class="contact-line">
        <svg viewBox="0 0 24 24" fill="none" stroke="#fff" stroke-width="2"><circle cx="12" cy="12" r="9"/><path d="M3 12h18M12 3c3 3 3 15 0 18M12 3c-3 3-3 15 0 18"/></svg>
        www.cornerway.org
      </p>
      <p class="address">421, Address line goes here<br>45452, Country Name</p>
    </div>
  </section>

</body>
</html>
```